Modern Design for Eyecare business - Vision Center, Optometry, Eye Doctors, Health Care

Create a sleek, modern, sharp homepage design for a eyecare center in Oklahoma City, OK. The vision center provides eyecare health services along with prescription eyewear.

I have included the logo which should be the basis of the designs look and feel. No other imagery was given so feel free to include stock photos and illustrations that you believe give the design a fresh look.

Please do not include stock photos of people/humans

I have included a document that provides some verbiage for the design as well as the designs main navigation.

They have an existing website http://www.brightmeadowvision.example/ but are not happy with it. The new design should be different than their existing design.

List of websites for inspiration:
http://www.oak.gathering
https://www.harborlenspartners.example
http://www.sunvaledental.example/
https://www.plumo.example

Target Market(s)

all ages

industry: Health, Eyewear, Eyecare, Optometry

Industry/Entity Type

Health

Number of Pages Required

1 page

Requirements
Must have
• Light color scheme that matches logo colors.
• Sophisticated, sleek design that resembles the logo's style.
Nice to have
• Large, full width visual banner with a 'contact us, etc' call-to-action between header and homepage content
Should not have
• No stock images of people/humans.
• Other forms of stock photos/illustrations are fine.

```html
<!DOCTYPE html>
<html lang="en">
<head>
<meta charset="utf-8">
<title>Brightmeadow Vision</title>
<link href="https://fonts.googleapis.com/css2?family=Open+Sans:wght@400;600;700&family=Raleway:wght@400;500;600;700&display=swap" rel="stylesheet">
<style>
:root{
  --navy:#2f4159;
  --navy-deep:#243449;
  --blue:#6c8fc8;
  --blue-soft:#7f9ed0;
  --mist:#e4e8ec;
  --white:#ffffff;
  --text:#5b6470;
  --star:#f39c12;
}
*{margin:0;padding:0;box-sizing:border-box}
html,body{width:1200px;height:2568px;overflow:hidden;background:var(--white)}
body{font-family:"Open Sans",Arial,sans-serif;color:var(--text)}
.page{position:relative;width:1200px;height:2568px;overflow:hidden}
.abs{position:absolute}

/* hero */
.hero-visual{left:0;top:0;width:1200px;height:800px;
  background:radial-gradient(ellipse at 55% 50%,#5e9fb4 0%,#8fbccd 25%,#bcd6e3 50%,#dfe9f1 80%,#eef3f8 100%)}
.brand{left:77px;top:38px;display:flex;align-items:center;gap:14px}
.brand-dot{width:34px;height:34px;border-radius:50%;background:var(--navy)}
.brand-name{font-family:"Raleway",sans-serif;font-weight:500;font-size:32px;color:var(--navy)}
.nav{left:443px;top:45px;display:flex;font-family:"Raleway",sans-serif;font-size:19px;color:var(--navy)}
.nav a{display:block;height:51px;line-height:51px;padding:0 17px;color:inherit;text-decoration:none}
.nav a.active{background:var(--blue);color:var(--white)}
.hero-title{left:0;top:250px;width:1200px;text-align:center;font-family:"Raleway",sans-serif;font-weight:700;font-size:68px;line-height:104px;color:var(--white)}
.hero-btn{left:437px;top:486px;width:326px;height:55px;background:var(--white);color:var(--navy);font-family:"Raleway",sans-serif;font-size:20px;line-height:55px;text-align:center}

/* features */
.features{left:0;top:800px;width:1200px;height:374px;background:var(--mist)}
.feature{width:360px;text-align:center;top:732px}
.feature-icon{width:136px;height:136px;border-radius:50%;background:var(--navy);margin:0 auto;display:flex;align-items:center;justify-content:center;color:var(--white);font-family:"Open Sans",sans-serif;font-weight:700;font-size:80px}
.feature h3{margin-top:20px;font-family:"Raleway",sans-serif;font-weight:400;font-size:23px;line-height:31px;color:var(--blue)}
.feature p{margin-top:10px;font-size:15.5px;line-height:25px;color:var(--text);padding:0 20px}
.pill{display:inline-block;background:var(--navy);color:var(--white);font-family:"Raleway",sans-serif;font-size:18px;height:52px;line-height:52px;padding:0 27px;border-radius:26px;margin-top:18px}

/* welcome */
.welcome{left:0;top:1222px;width:1200px;text-align:center}
.welcome h2{font-family:"Raleway",sans-serif;font-weight:400;font-size:44px;color:var(--navy)}
.welcome h2 span,.review h2 span{color:var(--blue)}
.welcome p{margin:16px auto 0;width:860px;font-size:21px;line-height:31px;color:var(--blue)}
.welcome .pill{margin-top:30px;padding:0 28px}

/* call band */
.callband{left:77px;top:1489px;width:1046px;height:146px;background:var(--blue)}
.callband svg{position:absolute;left:0;top:0}
.call-icon{left:46px;top:34px;width:62px;height:62px;border-radius:50%;background:var(--white);display:flex;align-items:center;justify-content:center}
.call-label{left:120px;top:34px;color:var(--white);font-family:"Raleway",sans-serif;font-size:20px}
.call-number{left:118px;top:56px;color:var(--white);font-family:"Open Sans",sans-serif;font-weight:700;font-size:38px}
.call-slogan{left:440px;top:28px;color:var(--white);font-family:"Raleway",sans-serif;font-size:31px}
.call-btn{left:444px;top:74px;height:50px;line-height:50px;padding:0 30px;border-radius:25px;background:var(--navy);color:var(--white);font-family:"Raleway",sans-serif;font-size:22px}

/* review */
.review{left:0;top:1680px;width:1200px;text-align:center}
.review h2{font-family:"Raleway",sans-serif;font-weight:400;font-size:40px;color:var(--navy)}
.review .quote{margin-top:8px;font-family:Georgia,serif;font-weight:700;font-size:48px;line-height:40px;color:var(--navy)}
.review p{margin:8px auto 0;width:830px;font-size:15.5px;line-height:26px;color:var(--text)}
.review .who{margin-top:16px;font-weight:700;font-size:15.5px;color:var(--navy)}
.stars{margin-top:8px;color:var(--star);font-size:24px;letter-spacing:1px}
.arrow{top:1784px;width:62px;height:62px;border:1.5px solid var(--navy);border-radius:50%;display:flex;align-items:center;justify-content:center}

/* contact */
.contact{left:0;top:1964px;width:1200px;height:553px;background:radial-gradient(ellipse at 50% 60%,#4d5f73 0%,#35475c 55%,#26374b 100%)}
.contact h2{position:absolute;left:0;top:72px;width:1200px;text-align:center;font-family:"Raleway",sans-serif;font-weight:400;font-size:41px;color:var(--white)}
.field{left:79px;width:435px;height:50px;border:1.5px solid var(--white);border-radius:4px;color:var(--white);font-size:15px;padding:11px 10px}
.submit{left:79px;top:2412px;width:164px;height:50px;border-radius:25px;background:var(--white);color:var(--navy);font-family:"Raleway",sans-serif;font-size:24px;line-height:50px;text-align:center}
.map{left:536px;top:2120px;width:276px;height:274px;background:linear-gradient(135deg,#e8e6df,#d7dccf 50%,#ece9e2)}
.info{left:856px;top:2118px;color:var(--white);font-size:15.5px}
.info h4{font-family:"Raleway",sans-serif;font-weight:400;font-size:21px;margin-bottom:14px}
.info-row{display:flex;gap:12px;align-items:flex-start;margin-bottom:14px;line-height:24px}
.info-row svg{flex:none;margin-top:4px}
.info a{color:var(--white);font-weight:700;text-decoration:underline}

.footer{left:0;top:2517px;width:1200px;height:51px;background:var(--blue);color:var(--white);text-align:center;line-height:51px;font-size:15px}
</style>
</head>
<body>
<div class="page">

  <div class="abs hero-visual" role="img" aria-label="Close-up stock photograph of a blue eye with a scanning light overlay"></div>
  <div class="abs brand"><span class="brand-dot"></span><span class="brand-name">Brightmeadow Vision</span></div>
  <nav class="abs nav">
    <a class="active">HOME</a><a>VISION</a><a>PATIENT</a><a>SCHEDULE APPOINTMENT</a><a>CONTACT</a>
  </nav>
  <h1 class="abs hero-title">COMITTED TO EXCELLENCE<br>IN VISION CARE</h1>
  <div class="abs hero-btn">BOOK YOUR APPOINTMENT</div>

  <div class="abs features"></div>
  <div class="abs feature" style="left:49px">
    <div class="feature-icon">
      <svg width="74" height="46" viewBox="0 0 74 46"><path d="M3 23C14 7 26 3 37 3s23 4 34 20C60 39 48 43 37 43S14 39 3 23Z" fill="none" stroke="#fff" stroke-width="5"/><circle cx="37" cy="23" r="12" fill="#fff"/><circle cx="37" cy="23" r="5" fill="#2f4159"/></svg>
    </div>
    <h3>TRUE EXPERTS OF EYE CARE</h3>
    <p>Many people resort to the simple solution of purchasing glasses at a drug store or pharmacy, but it could cost...</p>
    <span class="pill">READ MORE</span>
  </div>
  <div class="abs feature" style="left:419px">
    <div class="feature-icon">
      <svg width="70" height="70" viewBox="0 0 70 70"><circle cx="30" cy="30" r="20" fill="none" stroke="#fff" stroke-width="6"/><path d="M44 44 62 62" stroke="#fff" stroke-width="9" stroke-linecap="round"/></svg>
    </div>
    <h3>PERSONALIZED PATIENT<br>CARE &amp; TREATMENT</h3>
    <p>Refractive errors and other eye problems are common; however, not all ocular conditions are the same.</p>
    <span class="pill">READ MORE</span>
  </div>
  <div class="abs feature" style="left:779px">
    <div class="feature-icon">?</div>
    <h3>Why Us?</h3>
    <p>We treat you like a VIP - every experience you have with us will leave you knowing you received the VIP treatment</p>
    <span class="pill">READ MORE</span>
  </div>

  <section class="abs welcome">
    <h2><span>WELCOME TO</span> BRIGHTMEADOW VISION</h2>
    <p>Sight is precious... Don't you think? We would love to have the opportunity to care foryour family's vision. Most of all, we want you to know that.... WE CARE!</p>
    <span class="pill">READ MORE</span>
  </section>

  <div class="abs callband">
    <svg width="1046" height="146" viewBox="0 0 1046 146"><path d="M0 0H425C385 0 380 40 385 73C390 110 370 146 330 146H0Z" fill="#2f4159"/><path d="M425 0C395 6 392 40 396 73C400 110 385 146 350 146" fill="none" stroke="#fff" stroke-width="6"/></svg>
    <div class="abs call-icon"><svg width="30" height="30" viewBox="0 0 24 24"><path d="M6.6 10.8a15 15 0 0 0 6.6 6.6l2.2-2.2c.3-.3.7-.4 1-.2 1.1.4 2.3.6 3.6.6.6 0 1 .4 1 1V20c0 .6-.4 1-1 1A17 17 0 0 1 3 4c0-.6.4-1 1-1h3.5c.6 0 1 .4 1 1 0 1.3.2 2.5.6 3.6.1.3 0 .7-.2 1Z" fill="#2f4159"/></svg></div>
    <div class="abs call-label">CALL US NOW!</div>
    <div class="abs call-number">405 555 0142</div>
    <div class="abs call-slogan">Committed To Excellence In Vision Care</div>
    <div class="abs call-btn">Appointment Request</div>
  </div>

  <section class="abs review">
    <h2><span>PATIENT</span> REVIEW</h2>
    <div class="quote">&ldquo;</div>
    <p>Dr. Hollins is very personable and fast, without making you feel rushed. The staff is all very friendly, professional and efficient. They also help to make decisions on eye are solutions that fit your budget.</p>
    <div class="who">- Ferro, Oklahoma City</div>
    <div class="stars">★★★★★</div>
  </section>
  <div class="abs arrow" style="left:79px"><svg width="20" height="34" viewBox="0 0 20 34"><path d="M16 2 3 17l13 15" fill="none" stroke="#2f4159" stroke-width="2"/></svg></div>
  <div class="abs arrow" style="left:1060px"><svg width="20" height="34" viewBox="0 0 20 34"><path d="M4 2l13 15L4 32" fill="none" stroke="#2f4159" stroke-width="2"/></svg></div>

  <section class="abs contact" role="img" aria-label="Stock photograph of eyeglasses over a blurred forest, tinted dark blue">
    <h2>CONTACT US</h2>
  </section>
  <div class="abs field" style="top:2121px">Name</div>
  <div class="abs field" style="top:2178px">E-Mail</div>
  <div class="abs field" style="top:2236px">Phone</div>
  <div class="abs field" style="top:2292px;height:102px">Message</div>
  <div class="abs submit">SUBMIT</div>
  <div class="abs map" role="img" aria-label="Street map showing the clinic location"></div>
  <div class="abs info">
    <h4>CONTACT INFO</h4>
    <div class="info-row"><svg width="16" height="20" viewBox="0 0 16 20"><path d="M8 0a7 7 0 0 0-7 7c0 5 7 13 7 13s7-8 7-13a7 7 0 0 0-7-7Zm0 10a3 3 0 1 1 0-6 3 3 0 0 1 0 6Z" fill="#fff"/></svg><div>2150 North Larkin Blvd.<br>Oklahoma City, OK 73118<br><a>VIEW MAP</a></div></div>
    <div class="info-row"><svg width="18" height="18" viewBox="0 0 24 24"><path d="M6.6 10.8a15 15 0 0 0 6.6 6.6l2.2-2.2c.3-.3.7-.4 1-.2 1.1.4 2.3.6 3.6.6.6 0 1 .4 1 1V20c0 .6-.4 1-1 1A17 17 0 0 1 3 4c0-.6.4-1 1-1h3.5c.6 0 1 .4 1 1 0 1.3.2 2.5.6 3.6.1.3 0 .7-.2 1Z" fill="#fff"/></svg><div>405-555-0142</div></div>
    <div class="info-row"><svg width="18" height="18" viewBox="0 0 18 18"><rect x="1" y="6" width="16" height="10" rx="1" fill="none" stroke="#fff" stroke-width="2"/><rect x="5" y="1" width="8" height="6" fill="none" stroke="#fff" stroke-width="2"/></svg><div>405-555-0187</div></div>
    <div class="info-row"><svg width="18" height="14" viewBox="0 0 18 14"><rect x="1" y="1" width="16" height="12" fill="none" stroke="#fff" stroke-width="2"/><path d="M1 1l8 7 8-7" fill="none" stroke="#fff" stroke-width="2"/></svg><div>info@brightmeadowvision.example</div></div>
  </div>

  <footer class="abs footer">© BRIGHTMEADOW VISION - 2016. All Rights Reserved.</footer>
</div>
</body>
</html>
```